The Velvet Needle Poster for a shop Facade

Hello Designers,

• We have a 4X4 meters façade for our tailor shop “The Velvet Needle”, and we are looking for a unique, simple and attractive poster to be printed on the glass to attract the attention of the driving customers or whoever passes by the shop.
• The Velvet Needle, with ‘Velvet’ referring to door-to-door service, our concept as follows (Call … Measure … Stitch … Deliver)

1. Step1: Book online or simply call us to make your appointment (should be pictorial not writing)
2. Step2: Our dedicated personnel will come to you at your preferred time and location. (should be pictorial not writing)
3. Step3: Clothes Alteration/Making to suit your style and body fit. (should be pictorial not writing)
4. Step4: Delivery on completion, at your preferred time and location. (should be pictorial not writing)

• We are specialized in clothes alteration and making for both men and women, and anything related to tailoring services www.thevelvetneedle.example

• The poster must include the name “The Velvet Needle” as well as the phone number 04 318 2976 in a very clear and obvious way (logo will be optional if you can show it in a nice way)
And the concept of our shop should be shown in the poster in a very simple and clear way and more graphical than words. (Perhaps a graphical flow to show client booking our service and we go to their place for alterations done).
Colors should be chosen carefully to attract the customers and the walk-ins eyes when they pass by either walking or by cars.

Thank you
Omar

Target Market(s)

We have a 4X4 meters façade for our tailor shop “The Velvet Needle”, and we are looking for a unique, simple and attractive poster to be printed on the glass to attract the attention of the driving customers or whoever passes by the shop.

Industry/Entity Type

Fashion

• to match the poster/signage

Colors

Designer to choose colors to be used in the design.

Requirements
Must have
Nice to have
• the concept of our shop should be shown in the poster in a very simple and clear way and more graphical than words. (Perhaps a graphical flow to show client booking our service and we go to their place for alterations done).
Should not have
• many words, copied designs. Please only use the images attached in the project brief for reference.

```html
<!DOCTYPE html>
<html lang="en">
<head>
<meta charset="utf-8">
<title>The Velvet Needle – Clothes Alterations</title>
<link rel="stylesheet" href="https://fonts.googleapis.com/css2?family=Josefin+Sans:wght@300;400&family=Montserrat:wght@600&family=Poiret+One&display=swap">
<style>
  :root {
    --charcoal: #3a3a3c;
    --paper: #f2f2f4;
    --ink: #333335;
    --line: #e6e6e8;
    --wood-dark: #3b2218;
    --wood-mid: #5a3525;
    --thread-blue: #2c4f7a;
    --thread-red: #8e2a2e;
  }
  * { box-sizing: border-box; margin: 0; padding: 0; }
  html, body { width: 1200px; height: 1200px; overflow: hidden; background: var(--charcoal); }
  .poster { position: relative; width: 1200px; height: 1200px; background: var(--charcoal); color: var(--paper); font-family: "Josefin Sans", sans-serif; font-weight: 300; }

  .workbench-photo {
    position: absolute; left: 0; top: 0; width: 1200px; height: 388px;
    background: linear-gradient(90deg, var(--wood-dark) 0%, var(--wood-mid) 40%, #4a3a36 62%, var(--thread-blue) 80%, var(--thread-red) 100%);
  }
  .frame { position: absolute; left: 31px; top: 31px; width: 1139px; height: 1063px; border: 1px solid var(--line); border-bottom: none; }

  .brand-disc {
    position: absolute; left: 101px; top: 88px; width: 474px; height: 474px; border-radius: 50%;
    background: var(--paper); display: flex; flex-direction: column; align-items: center; justify-content: center;
    color: var(--ink); font-weight: 300; text-align: center;
  }
  .brand-name { font-size: 62px; line-height: 1.15; letter-spacing: 2px; }

  .headline { position: absolute; left: 600px; top: 432px; width: 540px; text-align: center; font-family: "Poiret One", sans-serif; font-size: 54px; line-height: 63px; letter-spacing: 16px; }

  .process-bar { position: absolute; left: 89px; top: 602px; width: 1022px; height: 65px; border-top: 1.5px solid var(--line); border-bottom: 1.5px solid var(--line); display: flex; align-items: center; justify-content: space-between; font-family: "Montserrat", sans-serif; font-weight: 600; font-size: 35px; letter-spacing: 10px; }
  .process-bar span:last-child { letter-spacing: 10px; margin-right: -10px; }

  .steps { position: absolute; left: 31px; top: 723px; width: 1139px; height: 317px; display: flex; }
  .step { flex: 1; display: flex; flex-direction: column; align-items: center; padding: 30px 18px 0; border-right: 1.5px solid var(--line); }
  .step:last-child { border-right: none; }
  .step-icon { width: 120px; height: 120px; }
  .step-title { margin-top: 26px; font-size: 27px; font-weight: 400; letter-spacing: 1.5px; }
  .step-title b { font-weight: 400; }
  .step-text { margin-top: 24px; font-size: 16px; line-height: 15px; letter-spacing: 0.8px; text-align: center; }

  .contact-band { position: absolute; left: 0; top: 1094px; width: 1200px; height: 106px; background: var(--paper); color: var(--ink); display: flex; align-items: center; padding: 6px 42px 0; }
  .website { font-size: 35px; font-weight: 400; letter-spacing: 1.5px; }
  .band-divider { width: 2px; height: 52px; background: var(--ink); margin: 0 24px; }
  .phone { font-size: 66px; font-weight: 400; letter-spacing: 4px; white-space: nowrap; }
</style>
</head>
<body>
<div class="poster">
  <div class="workbench-photo" role="img" aria-label="Photo of a tailor's hands sorting buttons and spools of coloured thread beside scissors on a wooden table"></div>
  <div class="frame"></div>

  <div class="brand-disc">
    <div class="brand-name">The Velvet<br>Needle</div>
  </div>

  <h1 class="headline" style="font-weight:400">Clothes<br>Alterations</h1>

  <div class="process-bar">
    <span>CALL</span><span>|</span><span>MEASURE</span><span>|</span><span>STITCH</span><span>|</span><span>DELIVER</span>
  </div>

  <div class="steps">
    <div class="step">
      <svg class="step-icon" viewBox="0 0 120 120" fill="none" stroke="#f2f2f4" stroke-width="3" stroke-linejoin="round">
        <path d="M14 18c6-8 14-10 18-6l14 18c3 4 1 8-3 11l-6 5c5 14 17 27 31 33l6-6c3-3 7-4 10-1l18 13c4 4 2 12-7 18-10 7-26 2-44-12C28 78 12 54 10 38c-1-8 0-14 4-20z"/>
      </svg>
      <div class="step-title">STEP <b>1</b></div>
      <p class="step-text">Book online or simply call us to make your appointment</p>
    </div>
    <div class="step">
      <svg class="step-icon" viewBox="0 0 120 120" fill="none" stroke="#f2f2f4" stroke-width="3" stroke-linejoin="round">
        <path d="M46 12c14 0 22 10 20 24-1 8-4 14-8 18v8c10 4 16 6 20 10v34H10v-8c0-10 8-14 22-18l10-4v-8c-5-5-8-12-8-20 0-8 4-16 12-16z"/>
        <rect x="82" y="40" width="14" height="64" transform="rotate(18 89 72)"/>
        <path d="M98 42l10 4-16 52-6 8-2-10z"/>
      </svg>
      <div class="step-title">STEP <b>2</b></div>
      <p class="step-text">Our dedicated personnel will come to you at your preferred time and location</p>
    </div>
    <div class="step">
      <svg class="step-icon" viewBox="0 0 120 120" fill="none" stroke="#f2f2f4" stroke-width="3" stroke-linejoin="round">
        <ellipse cx="52" cy="36" rx="26" ry="20" transform="rotate(-40 52 36)"/>
        <ellipse cx="52" cy="36" rx="9" ry="7" transform="rotate(-40 52 36)"/>
        <path d="M30 54l58 58 16-16-36-36"/>
        <path d="M44 68l6-6M54 78l8-8M64 88l6-6M74 98l8-8"/>
      </svg>
      <div class="step-title">STEP <b>3</b></div>
      <p class="step-text">Clothes Alteration/Making to suit your style and body fit</p>
    </div>
    <div class="step">
      <svg class="step-icon" viewBox="0 0 120 120" fill="none" stroke="#f2f2f4" stroke-width="3" stroke-linejoin="round" stroke-linecap="round">
        <path d="M22 34h54v50H28M76 48h20l14 18v18h-8M76 84h12"/>
        <path d="M4 52h30M10 64h20M2 76h16"/>
        <circle cx="40" cy="88" r="7"/><circle cx="96" cy="88" r="7"/>
      </svg>
      <div class="step-title">STEP <b>4</b></div>
      <p class="step-text">Delivery on completion, at your preferred time and location</p>
    </div>
  </div>

  <div class="contact-band">
    <span class="website">www.thevelvetneedle.example</span>
    <span class="band-divider"></span>
    <span class="phone">04 318 2976</span>
  </div>
</div>
</body>
</html>
```